Home Page Redesign for Pet Website

Looking to redesign the home page of our WORDPRESS website which will be renamed The Critter Cover Handbook 2015.

Looking for clean design which communicates clarity.
Updates

This is for a Wordpress site.

Please note that the design MUST include the content which is shown in the table in the brief!

Hi Thanks for the designs so far. We have just updated the brief to provide more information and clarify a few issues. We have also now included a couple of layout suggestions. They are just suggestions but it should give you a better idea of what we are looking for. And we have just increased the budget for 1st place by £120. Please feel free to message me if you have any questions. Many thanks. Maud

Please note that the new brief is in a file dated 25 Jan!

Reason: We have extended the deadline so we can continue working with the designers who have submitted designs we like. If you have any new designs please submit them by the original deadline of 7.37pm this evening (GMT). We are planning to make our final decision by Friday this week.

Target Market(s)

UK pet owners. All ages but largest age group is 35-50.

Industry/Entity Type

Insurance

Requirements
Must have
• Three clear content groups - LEARN, RESEARCH, CAMPAIGN (see brief for more details).
Stock photos with dogs and cats
Use current colour scheme
Must work with existing inner pages.
Existing font.. but 1pt larger
See brief for more details
Should not have
• Logo
Content from Existing Page (except for footer content... and menu headings).

```html
<!DOCTYPE html>
<html lang="en">
<head>
<meta charset="utf-8">
<title>The Critter Cover Handbook 2015</title>
<link href="https://fonts.googleapis.com/css2?family=Raleway:wght@400;500;600&family=Open+Sans:wght@400;600;700&display=swap" rel="stylesheet">
<style>
:root{
  --orange:#f47a20;
  --orange-light:#ff9a3c;
  --orange-deep:#f25a1a;
  --blue:#2f5fd0;
  --blue-deep:#1d3fb6;
  --navy:#141e5e;
  --navy-deep:#0d1548;
  --text:#333;
  --muted:#666;
  --line:#d8d8d8;
  --panel:#f3f3f3;
}
*{box-sizing:border-box;margin:0;padding:0}
html,body{width:776px;height:1200px;overflow:hidden}
body{position:relative;background:#fff;font-family:"Open Sans",sans-serif;color:var(--text);font-size:7px}
.abs{position:absolute}
h1,h2,h3,.raleway{font-family:"Raleway",sans-serif;font-weight:500}

.brand{left:103px;top:13px;font-family:"Raleway",sans-serif;font-size:14px;line-height:15px;font-weight:600}
.brand .l1{color:var(--orange)}
.brand .l2{color:var(--blue);padding-left:22px}
.social-top{right:106px;top:13px;display:flex;gap:6px;font-family:"Raleway",sans-serif;font-weight:600;font-size:8px;color:var(--blue)}
.search{left:534px;top:31px;width:140px;height:17px;border:1px solid #ccc;border-radius:2px;font-size:6px;color:#777;padding:4px 7px}
.search svg{position:absolute;right:6px;top:3px}

.nav{left:0;top:56px;width:776px;height:27px;background:linear-gradient(var(--orange-light),var(--orange));display:flex;padding-left:113px}
.nav a{color:#fff;text-decoration:none;font-family:"Raleway",sans-serif;font-size:8.5px;font-weight:500;line-height:27px;padding:0 11px;border-right:1px solid rgba(255,255,255,.35)}
.nav a:last-child{border:none}

.hero{left:0;top:83px;width:776px;height:270px;background:linear-gradient(180deg,#1b1b14 0%,#3a3a22 40%,#5d7a2a 75%,#7c9a3a 100%)}
.hero-pets{left:370px;top:83px;width:300px;height:270px;background:radial-gradient(ellipse at 55% 50%,#e9d2a8 0%,#c7a574 40%,rgba(80,70,40,0) 72%)}
.hero-card{left:102px;top:174px;width:246px;height:105px;background:rgba(29,70,190,.92);color:#fff;padding:17px 20px}
.hero-card h1{font-size:21px;font-weight:400;line-height:23px}
.hero-card h2{font-size:13px;color:#9ec2ff;font-weight:400;margin-top:1px}
.hero-card p{font-size:6px;line-height:10px;margin-top:6px;color:#e0e8ff}

.tile{top:373px;width:137px;height:122px;border-radius:4px;color:#fff;text-align:center;padding-top:12px}
.tile.blue{background:linear-gradient(160deg,#3b7ff0,var(--blue-deep))}
.tile.orange{background:linear-gradient(160deg,var(--orange-light),var(--orange-deep))}
.tile h3{font-size:11.5px;font-weight:400;line-height:13px;margin-top:6px}
.tile p{font-size:6px;line-height:10px;opacity:.85;margin-top:3px;padding:0 20px}
.tile svg{display:block;margin:0 auto}

.col{top:522px;height:232px;border:1px solid var(--line);border-radius:2px}
.col-head{height:38px;background:linear-gradient(#fafafa,#ececec);border-bottom:1px solid var(--line);padding:7px 22px;font-family:"Raleway",sans-serif}
.col-head .k{font-size:8.5px;color:#333}
.col-head .t{font-size:11px;color:var(--blue)}
.col-head .t.or{color:var(--orange)}
.col ul{list-style:none;padding:8px 22px}
.col li{font-size:6.5px;line-height:9px;margin-bottom:9px;color:#333}
.providers{display:grid;grid-template-columns:75px 75px;gap:0 0;padding:0 24px}
.providers span{font-size:6.5px;line-height:13.3px}

.popular{left:106px;top:792px;font-family:"Raleway",sans-serif;font-size:14px;color:#333}
.thumb{top:821px;width:77px;height:68px}
.article{top:821px;width:142px}
.article h4{font-family:"Raleway",sans-serif;font-weight:500;color:var(--orange);font-size:8px;line-height:10px}
.article p{font-size:6px;line-height:11px;color:#555;margin-top:2px}
.article .more{font-weight:600;color:#333;margin-top:4px;font-size:6px}
.ad{left:576px;top:800px;width:98px;height:98px;background:linear-gradient(160deg,#1f6aa8,#0b3768 60%,#164f86)}

.footer{left:0;top:951px;width:776px;height:214px;background:var(--navy)}
.copy{left:0;top:1165px;width:776px;height:35px;background:var(--navy-deep);color:#d0d4ea;font-size:6.5px;padding:12px 103px}
.widget{top:974px;width:134px;height:167px;background:#fff;border-radius:2px;overflow:hidden}
.widget-head{height:19px;background:#dfe4ef;font-family:"Raleway",sans-serif;font-size:8px;color:#222;padding:4px 12px;display:flex;align-items:center;gap:5px}
.widget-head.tw{background:#6fd0e6}
.dot{width:7px;height:7px;border-radius:50%;background:var(--blue)}
.avatar{width:20px;height:22px;background:#c9b9a9}
.ftitle{font-family:"Raleway",sans-serif;font-size:11px;color:#fff;font-weight:500}
.flinks{font-size:6.5px;color:#fff;line-height:15px}
.btn{display:inline-block;background:#3b5998;color:#fff;font-size:5.5px;font-weight:700;padding:1px 4px;border-radius:2px}
.btn.w{background:#fff;color:#333}
.disclaimer p{font-size:6px;line-height:11px;color:#c9cde6}
</style>
</head>
<body>

<header>
  <div class="abs brand"><div class="l1">The Critter Cover</div><div class="l2">Handbook 2015</div></div>
  <div class="abs social-top"><span>Chirper</span><span>Facepage</span><span>Linkpro</span></div>
  <div class="abs search">Search here
    <svg width="10" height="10" viewBox="0 0 10 10"><circle cx="4" cy="4" r="3" fill="none" stroke="#555" stroke-width="1.3"/><line x1="6.2" y1="6.2" x2="9" y2="9" stroke="#555" stroke-width="1.4"/></svg>
  </div>
  <nav class="abs nav">
    <a href="#">Home</a><a href="#">Pet Insurance Reviews</a><a href="#">Providers A-Z</a><a href="#">Pet Insurance Policies</a><a href="#">Surveys</a><a href="#">More</a>
  </nav>
</header>

<section>
  <div class="abs hero" role="img" aria-label="Photo of a puppy and a kitten on a sunny lawn"></div>
  <div class="abs hero-pets" aria-hidden="true"></div>
  <div class="abs hero-card">
    <h1>Pet Insurance Guide</h1>
    <h2>Curabitur iaculis tempus eros</h2>
    <p>Etiam est nunc venenatis in tristique eu imperdiet ac nisl Cum sociis natoque penatibus et magnis dis parturient</p>
  </div>
</section>

<section>
  <div class="abs tile blue" style="left:103px">
    <svg width="56" height="46" viewBox="0 0 56 46"><path d="M28 3c-2-3-7-1-6 3 1 3 6 6 6 6s5-3 6-6c1-4-4-6-6-3z" fill="#fff"/><path d="M8 22c4 0 6 2 12 2h14l4-6c2-2 6-2 7 0l3 3-3 2-2 0-2 8v13h-3l-1-10h-14l-2 10h-3v-12l-3-4c-3 0-6-1-8-6z" fill="#fff"/></svg>
    <h3>Pet Insurance<br>Provider</h3>
    <p>Lorem ipsum dolor sit amet consectetuer adipis</p>
  </div>
  <div class="abs tile blue" style="left:249px">
    <svg width="56" height="46" viewBox="0 0 56 46"><ellipse cx="17" cy="18" rx="5" ry="6" fill="#fff"/><ellipse cx="24" cy="9" rx="5" ry="6" fill="#fff"/><ellipse cx="33" cy="9" rx="5" ry="6" fill="#fff"/><ellipse cx="40" cy="18" rx="5" ry="6" fill="#fff"/><path d="M28 20c-7 0-12 9-12 14 0 5 5 6 12 4 7 2 12 1 12-4 0-5-5-14-12-14z" fill="#fff"/></svg>
    <h3>Pet Insurance<br>Reviews</h3>
    <p>Lorem ipsum dolor sit amet consectetuer adipis cing</p>
  </div>
  <div class="abs tile orange" style="left:394px">
    <svg width="56" height="46" viewBox="0 0 56 46"><circle cx="28" cy="23" r="15" fill="#fff"/><path d="M21 23l5 5 9-10" fill="none" stroke="#f47a20" stroke-width="4" stroke-linecap="round" stroke-linejoin="round"/></svg>
    <h3>Top Policies</h3>
    <p>Lorem ipsum dolor sit amet consectetuer adipis cing elit Nam cursus Morbi Nullam</p>
  </div>
  <div class="abs tile orange" style="left:540px">
    <svg width="56" height="46" viewBox="0 0 56 46"><circle cx="26" cy="19" r="11" fill="none" stroke="#fff" stroke-width="5"/><line x1="34" y1="27" x2="41" y2="35" stroke="#fff" stroke-width="6" stroke-linecap="round"/></svg>
    <h3>Search Policy</h3>
    <p>Lorem ipsum dolor sit amet consectetuer adipis cing elit Nam cursus Morbi Nullam</p>
  </div>
</section>

<section>
  <div class="abs col" style="left:102px;width:186px">
    <div class="col-head"><div class="k">Learn</div><div class="t">About Pet Insurance</div></div>
    <ul>
      <li>Introduction to Pet Insurance</li>
      <li>Vet Fees Cover Types</li>
      <li>What to Consider before Buying</li>
      <li>Ten Popular Pet Insurance Providers</li>
      <li>Confused by Pet Insurance: Start Here!</li>
      <li>Third Party Liability Insurance</li>
      <li>Six Vet Fees Pet Insurance Companies Won't Pay!</li>
      <li>Why Cheap Pet Insurance is Risky</li>
      <li>Why Your Pets Vet History is Important</li>
    </ul>
  </div>
  <div class="abs col" style="left:291px;width:188px">
    <div class="col-head"><div class="k">Research</div><div class="t or">UK Pet Insurance</div></div>
    <div style="padding:8px 24px 5px;font-size:6.5px;font-weight:600">Analysis, Customer Reviews</div>
    <div class="providers">
      <div><span>Paws Mutual</span><br><span>Harbour</span><br><span>Straight Cover</span><br><span>F&amp;K</span><br><span>Hearty Pets</span><br><span>Coverwell</span><br><span>Marlow &amp; Finch</span><br><span>QT=</span></div>
      <div style="padding-top:3px"><span>Kennel Circle</span><br><span>R&amp;T</span><br><span>Beyond Plus</span><br><span>Petwise</span><br><span>Hartley's</span><br><span>Fenco</span><br><span>Bright Money</span></div>
    </div>
    <ul style="padding-top:4px">
      <li>Search our database for policies matching your criteria</li>
      <li>Compare claims experiences for pet insurance providers</li>
    </ul>
  </div>
  <div class="abs col" style="left:482px;width:187px">
    <div class="col-head"><div class="k">Campaign</div><div class="t">For Fairer Pet Insurance</div></div>
    <ul style="padding-top:13px">
      <li>This section will contain paragraphs of text</li>
      <li>Brief explanation of why a campaign is needed.</li>
      <li>Brief explanation of what to campaign for.</li>
      <li>Bio pic of me... plus brief bio.</li>
      <li>How you can help</li>
      <li>Stories with Pet Pics.</li>
    </ul>
  </div>
</section>

<section>
  <h2 class="abs popular">Popular Articles and Resources</h2>
  <div class="abs thumb" style="left:106px;background:linear-gradient(#b8cfe0,#7ea64c)" role="img" aria-label="Photo of a small dog running on grass"></div>
  <div class="abs article" style="left:190px">
    <h4>Pet Insurance for Pre-Existing Conditions</h4>
    <p>Aascetur ridiculus mus In iaculis facilisis massa Etiam eu urna Sed porta Suspendisse quam leo molestie sed luctus quis feugiat in pede Fusce tellus Sed metus</p>
    <div class="more">Read More</div>
  </div>
  <div class="abs thumb" style="left:342px;background:linear-gradient(135deg,#3a2a1c,#9a7350 60%,#4a3424)" role="img" aria-label="Photo of a sleeping brown dog"></div>
  <div class="abs article" style="left:426px;top:819px">
    <h4>Pet Insurance for Pre-Existing Conditions</h4>
    <p>Aascetur ridiculus mus In iaculis facilisis massa Etiam eu urna Sed porta Suspendisse quam leo molestie sed luctus quis feugiat in pede Fusce tellus Sed metus</p>
    <div class="more">Read More</div>
  </div>
  <div class="abs ad" role="img" aria-label="Advertisement banner for Hostline Nile web hosting packages"></div>
</section>

<footer>
  <div class="abs footer"></div>

  <div class="abs widget" style="left:103px">
    <div class="widget-head"><span class="dot"></span>Join Us on Facepage</div>
    <div style="display:flex;gap:6px;padding:5px 6px">
      <div class="avatar" role="img" aria-label="Profile photo"></div>
      <div><div style="font-size:6px;font-weight:700;color:var(--blue-deep)">Critter Cover Surveys UK</div><div style="margin-top:3px;font-size:5.5px"><span class="btn">Like</span> 1,176</div></div>
    </div>
    <div style="margin:2px 6px;border:1px solid #ddd;height:100px;padding:5px;font-size:5.8px;line-height:8.5px;overflow:hidden">
      <div style="display:flex;gap:5px"><div class="avatar" style="width:15px;height:16px" role="img" aria-label="Profile photo"></div><div><div style="font-weight:700;color:var(--blue-deep)">Critter Cover Surveys UK</div><div style="color:#888;font-size:5px">January 19 at 1:13pm</div></div></div>
      <p style="margin-top:4px">Pet Insurance Premium Increases</p>
      <p style="margin-top:3px">Interesting article from Consumer Watch suggesting that that pet insurance premiums can double as your pet ages...</p>
      <p style="margin-top:3px">Have to confess that this sounds on the low side to me! Would be really</p>
    </div>
  </div>

  <div class="abs widget" style="left:256px">
    <div class="widget-head tw"><span class="dot" style="background:#fff"></span>Latest from Chirper</div>
    <div style="padding:4px 6px;font-size:6px;font-weight:600;display:flex;justify-content:space-between;border-bottom:1px solid #eee">Tweets <span class="btn w" style="border:1px solid #ccc">Follow</span></div>
    <div style="padding:3px 6px;font-size:5.5px;color:var(--blue)">pawfinder.example/dog-blog.php?d...</div>
    <div style="padding:10px 6px 0;font-size:5.5px;line-height:7.5px;display:flex;gap:4px">
      <div class="avatar" style="width:12px;height:13px;flex:none" role="img" aria-label="Profile photo"></div>
      <div><div style="font-weight:700">Critter Cover Surveys <span style="float:right;font-weight:400;color:#888;margin-left:12px">16 Jun</span></div><div style="color:#888">@CritterSurveys</div>
      <p>RT <span style="color:var(--blue)">@listeningpups</span>: Not into football? We have 14 adorable hearing dog puppies who will change your mind <span style="color:var(--blue)">#SummerCup</span> <span style="color:var(--blue)">pic.chirper.example/Kd82m</span></p></div>
    </div>
    <div style="margin:4px 6px 0;height:28px;background:linear-gradient(#4a8a2c,#c9c3b0)" role="img" aria-label="Photo of puppies lying on grass"></div>
    <div style="margin:4px 3px;border:1px solid #ccc;font-size:5.5px;color:#666;padding:3px 4px">Tweet to @CritterSurveys</div>
  </div>

  <div class="abs" style="left:415px;top:976px">
    <div class="ftitle">Follow Us</div>
    <div style="margin-top:4px"><span class="btn" style="background:#4a90d9">Follow @CritterSurveys</span></div>
    <div style="margin-top:3px"><span class="btn">Like</span></div>
    <div style="margin-top:3px"><span class="btn w">&nbsp;Circleup&nbsp;&nbsp;Follow&nbsp;</span></div>
    <div class="flinks" style="margin-top:6px">About Us<br>Legal Information &amp; Disclaimers<br>Privacy Policy</div>
  </div>

  <div class="abs disclaimer" style="left:543px;top:975px;width:134px">
    <div class="ftitle">Disclaimer</div>
    <p style="margin-top:4px">Please note that pet insurance terms often change. Whilst we will do our best to keep this website up to date you must check with the appropriate insurer before making any decisions. If you find any mistakes on this website please do let us know so we can correct it for the benefit of future visitors. Many thanks! - See more at:</p>
  </div>

  <div class="abs copy">Copyright © 2015. Critter Cover Surveys UK. All Right Reserved.</div>
</footer>

</body>
</html>
```